Medical Company in need of Modern business card design for new Wound Care clinic.

Modern business card design for our Woundcare company. Logo and description of services can be found on our website; https://www.tovrel-woundcare.com/

```html
<!DOCTYPE html>
<html lang="en">
<head>
<meta charset="utf-8">
<title>Tovrel Woundcare – Business Card</title>
<link rel="stylesheet" href="https://fonts.googleapis.com/css2?family=Montserrat:wght@400;500;700;800&family=Roboto:wght@400&display=swap">
<style>
  :root {
    --stage: #2b2b2c;
    --card: #1f1f20;
    --card-edge: #3a3a3c;
    --pattern-dark: #161617;
    --pattern-light: #2c2c2e;
    --gold: #c8922f;
    --white: #f4f4f4;
  }
  * { margin: 0; padding: 0; box-sizing: border-box; }
  html, body { width: 1200px; height: 694px; overflow: hidden; background: var(--stage); }
  .stage { position: relative; width: 1200px; height: 694px; }

  .card {
    position: absolute; top: 192px; width: 540px; height: 310px;
    background: var(--card); overflow: hidden;
  }
  .card--back { left: 40px; }
  .card--front { left: 620px; border: 6px solid var(--card-edge); }

  /* back */
  .pattern {
    position: absolute; left: 0; width: 100%; height: 90px;
    background: linear-gradient(135deg, var(--pattern-dark), var(--pattern-light) 50%, var(--pattern-dark));
  }
  .pattern--top { top: 0; }
  .pattern--bottom { bottom: 0; }
  .services {
    position: absolute; top: 90px; left: 0; width: 100%; height: 130px;
    display: flex; flex-direction: column; align-items: center; justify-content: center;
    text-align: center;
  }
  .services__title {
    font-family: "Montserrat", sans-serif; font-weight: 800; font-size: 16px;
    letter-spacing: 4px; color: var(--gold); margin-bottom: 10px;
  }
  .services__line {
    font-family: "Roboto", sans-serif; font-size: 11.5px; line-height: 17px; color: var(--white);
  }

  /* front */
  .identity { position: absolute; left: 34px; top: 30px; font-family: "Montserrat", sans-serif; }
  .brand { display: flex; align-items: center; gap: 10px; margin-bottom: 22px; }
  .brand__mark { width: 14px; height: 14px; background: var(--gold); }
  .brand__name { font-weight: 500; font-size: 18px; letter-spacing: 4px; color: var(--gold); }
  .person__name { font-weight: 800; font-size: 24px; color: var(--gold); letter-spacing: 0.5px; }
  .person__role { font-weight: 400; font-size: 13px; color: var(--white); letter-spacing: 0.5px; margin-bottom: 22px; }
  .contact { list-style: none; }
  .contact__item {
    display: flex; align-items: center; gap: 10px;
    font-size: 12.5px; color: var(--white); line-height: 21px;
  }
  .contact__icon { width: 14px; height: 14px; flex: none; }
  .address { margin-top: 12px; margin-left: 24px; font-size: 12.5px; line-height: 19px; color: var(--white); }
</style>
</head>
<body>
<div class="stage">

  <section class="card card--back">
    <div class="pattern pattern--top" role="img" aria-label="Tone-on-tone embossed brand pattern"></div>
    <div class="services">
      <h2 class="services__title">OUR SERVICES</h2>
      <p class="services__line">• Hyperbaric Oxygen Therapy (HBO): A Cornerstone of Advanced Wound Care</p>
      <p class="services__line">• Debridement • Advanced Wound Dressings • Bio-engineered Skin Substitutes</p>
      <p class="services__line">• Compression Therapy and Edema Management</p>
    </div>
    <div class="pattern pattern--bottom" role="img" aria-label="Tone-on-tone embossed brand pattern"></div>
  </section>

  <section class="card card--front">
    <div class="identity">
      <div class="brand">
        <span class="brand__mark"></span>
        <span class="brand__name">TOVREL WOUNDCARE</span>
      </div>
      <h1 class="person__name">MARCUS HALE</h1>
      <p class="person__role">MANAGING DIRECTOR</p>
      <ul class="contact">
        <li class="contact__item">
          <svg class="contact__icon" viewBox="0 0 24 24"><path fill="#c8922f" d="M6.6 10.8a15 15 0 0 0 6.6 6.6l2.2-2.2a1 1 0 0 1 1-.25 11.4 11.4 0 0 0 3.6.57 1 1 0 0 1 1 1V20a1 1 0 0 1-1 1A17 17 0 0 1 3 4a1 1 0 0 1 1-1h3.5a1 1 0 0 1 1 1c0 1.25.2 2.45.57 3.57a1 1 0 0 1-.25 1z"/></svg>
          044-555 210 347
        </li>
        <li class="contact__item">
          <svg class="contact__icon" viewBox="0 0 24 24"><rect x="2" y="5" width="20" height="14" fill="#c8922f"/><path d="M2 5l10 8 10-8" fill="none" stroke="#1f1f20" stroke-width="2"/></svg>
          hello@tovrel-woundcare.com
        </li>
        <li class="contact__item">
          <svg class="contact__icon" viewBox="0 0 24 24" fill="none" stroke="#c8922f" stroke-width="2"><circle cx="12" cy="12" r="9"/><path d="M3 12h18M12 3c3 3 3 15 0 18M12 3c-3 3-3 15 0 18"/></svg>
          www.tovrel-woundcare.com
        </li>
      </ul>
      <p class="address">88 Harlow Street, Suite 4<br>30417, Eastmere</p>
    </div>
  </section>

</div>
</body>
</html>
```